Clean and modern business cards

Looking for an updated business card design for my dental office “corvanta dental” . Looking for a modern clean / sleek design . I’m thinking black background but open to seeing other options . One side needs to have an appointment card . Card needs to have logo, dentist name , phone, email , address . I’ve attached couple of cards I thought were cool as well as my logo
Target Market(s)
Dental patients
Industry/Entity Type
Dentistry
Contact Information for Business Card
Phone email address

```html
<!DOCTYPE html>
<html lang="en">
<head>
<meta charset="utf-8">
<title>Corvanta Dental – Business Card</title>
<link href="https://fonts.googleapis.com/css2?family=Montserrat:wght@400;800;900&family=Quicksand:wght@400;500&display=swap" rel="stylesheet">
<style>
  :root {
    --ink: #060708;
    --paper: #ffffff;
    --card-light: #e6e7e7;
    --text-light: #e6e7e8;
    --accent-grey: #3a3b3d;
    --decor-tone: #c9c4cf;
  }
  * { margin: 0; padding: 0; box-sizing: border-box; }
  html, body { width: 1200px; height: 1200px; overflow: hidden; background: var(--paper); }
  .sheet { position: relative; width: 1200px; height: 1200px; }

  .card { position: absolute; left: 153px; width: 894px; height: 537px; }
  .card--front { top: 34px; background: var(--ink); color: var(--text-light); }
  .card--back { top: 629px; background: var(--card-light); color: var(--ink); }

  .el { position: absolute; }

  /* front */
  .brand-dot { left: 161px; top: 75px; width: 180px; height: 180px; border-radius: 50%; background: var(--accent-grey); }
  .brand-name { left: 380px; top: 128px; font-family: "Montserrat", sans-serif; font-weight: 800; color: var(--text-light); line-height: 1; text-align: right; }
  .brand-name__main { display: block; font-size: 60px; letter-spacing: 1px; }
  .brand-name__sub { display: block; font-size: 26px; letter-spacing: 14px; margin-top: 14px; margin-right: -14px; }

  .dentist-name { left: 0; width: 894px; top: 318px; text-align: center; font-family: "Montserrat", sans-serif; font-weight: 900; font-size: 42px; letter-spacing: 0.5px; }

  .contact { font-family: "Quicksand", sans-serif; font-weight: 500; font-size: 27px; line-height: 32px; display: flex; align-items: center; gap: 13px; }
  .contact__icon { width: 36px; height: 36px; flex: none; }
  .contact--email { left: 101px; top: 401px; }
  .contact--phone { left: 101px; top: 448px; }
  .contact--address { left: 462px; top: 401px; align-items: flex-start; }
  .contact--address .contact__icon { margin-top: 2px; }

  /* back */
  .brand-seal { left: 53px; top: 140px; width: 254px; height: 254px; border-radius: 50%; border: 3px solid var(--ink); display: flex; align-items: center; justify-content: center; text-align: center; font-family: "Montserrat", sans-serif; font-weight: 800; font-size: 28px; line-height: 1.25; letter-spacing: 1px; color: var(--ink); }
  .tooth-column { left: 336px; top: 169px; width: 26px; height: 199px; background: var(--decor-tone); border-radius: 13px; }

  .appt-pill { left: 378px; top: 71px; width: 464px; height: 70px; border-radius: 35px; background: var(--ink); color: var(--paper); display: flex; align-items: center; justify-content: center; font-family: "Montserrat", sans-serif; font-weight: 900; font-size: 38px; letter-spacing: 0.3px; }

  .field { left: 397px; font-family: "Montserrat", sans-serif; font-weight: 400; font-size: 36px; line-height: 1; }
  .field--date { top: 203px; }
  .field--time { top: 303px; }
  .field-line { left: 516px; width: 292px; height: 3px; background: var(--ink); }
  .field-line--date { top: 228px; }
  .field-line--time { top: 327px; }

  .policy { left: 0; width: 894px; top: 418px; text-align: center; font-family: "Quicksand", sans-serif; font-weight: 500; font-size: 26px; line-height: 32px; }
</style>
</head>
<body>
<main class="sheet">

  <section class="card card--front" aria-label="Business card front">
    <div class="el brand-dot" aria-hidden="true"></div>
    <div class="el brand-name">
      <span class="brand-name__main">CORVANTA</span>
      <span class="brand-name__sub">DENTAL</span>
    </div>

    <h1 class="el dentist-name">DR TEODOR VASKO</h1>

    <div class="el contact contact--email">
      <svg class="contact__icon" viewBox="0 0 36 36" aria-hidden="true">
        <circle cx="18" cy="18" r="18" fill="#e6e7e8"/>
        <rect x="8" y="11" width="20" height="14" rx="2" fill="none" stroke="#060708" stroke-width="2.4"/>
        <path d="M8.5 12 L18 19.5 L27.5 12" fill="none" stroke="#060708" stroke-width="2.4"/>
      </svg>
      <span>hello@corvantawpg.ca</span>
    </div>

    <div class="el contact contact--phone">
      <svg class="contact__icon" viewBox="0 0 36 36" aria-hidden="true">
        <circle cx="18" cy="18" r="18" fill="#e6e7e8"/>
        <path d="M24 8 L27 11 L23 15 L21 13 C18 16 16 19 15 22 L17 24 L13 28 L10 25 C11 17 16 12 24 8 Z" fill="#060708"/>
      </svg>
      <span>(204) 555 - 0172</span>
    </div>

    <div class="el contact contact--address">
      <svg class="contact__icon" viewBox="0 0 36 36" aria-hidden="true">
        <circle cx="18" cy="18" r="18" fill="#e6e7e8"/>
        <path d="M8 17 L18 8 L28 17 Z" fill="#060708"/>
        <rect x="10" y="19" width="16" height="10" fill="#060708"/>
      </svg>
      <span>2140 Brightwater AVE,<br>Winnipeg, MB</span>
    </div>
  </section>

  <section class="card card--back" aria-label="Appointment card back">
    <div class="el brand-seal">CORVANTA<br>DENTAL</div>
    <div class="el tooth-column" role="img" aria-label="Column of small outlined tooth icons"></div>

    <h2 class="el appt-pill">NEXT APPOINTMENT</h2>

    <div class="el field field--date">DATE:</div>
    <div class="el field-line field-line--date" aria-hidden="true"></div>
    <div class="el field field--time">TIME:</div>
    <div class="el field-line field-line--time" aria-hidden="true"></div>

    <p class="el policy">To cancel or reschedual please notify us atleast 48 hours prior<br>to your schedual appointment</p>
  </section>

</main>
</body>
</html>
```